KMRT timeline design

We need a facebook design for our established business which is Australia wide however based in Melbourne. We are a young team of Financial Planners who specialize in Insurance and Basic super advice for people like us.

We are people who help our clients get things done in a timely and cost effective manner whilst having a good time and a laugh along the way.

We do not want it to feel like the standard financial facebook page at all! We would like this to have a consistent feel with our new e-brochure which i have attached from a color and font perspective.

We would also like it to be very easy for people to be able to tell what we do from looking at the page

Reason: Would like time to respond to preferred designs and have re-works done before comitting

Target Market(s)

We work best with client from 25-40 who are time poor singles, young families and self-made entrepreneurs

Industry/Entity Type

Financial

```html
<!DOCTYPE html>
<html lang="en">
<head>
<meta charset="utf-8">
<title>KMRT timeline cover</title>
<link rel="stylesheet" href="https://fonts.googleapis.com/css2?family=Arimo:wght@400;700&display=swap">
<style>
  :root {
    --ink: #231f20;
    --green: #6cc24a;
    --green-deep: #3e9b2c;
    --green-light: #7fd45a;
    --white: #ffffff;
    --page: #ffffff;
    --btn-bg: #f6f7f9;
    --btn-border: #c5c6ca;
    --btn-text: #333333;
    --photo-dark: #3a3a3a;
    --photo-light: #a8a8a8;
  }
  * { margin: 0; padding: 0; box-sizing: border-box; }
  html, body { width: 1200px; height: 564px; overflow: hidden; background: var(--page); }
  body { font-family: "Arimo", Arial, sans-serif; position: relative; }

  .cover { position: absolute; left: 0; top: 0; width: 1200px; height: 450px; overflow: hidden; }
  .cover__photo {
    position: absolute; left: 300px; top: 0; width: 900px; height: 450px;
    background: linear-gradient(100deg, var(--photo-dark) 0%, #6e6e6e 35%, var(--photo-light) 60%, #7a7a7a 85%, #5a5a5a 100%);
  }
  .cover__band {
    position: absolute; left: 300px; top: 207px; width: 900px; height: 229px;
    background: rgba(20, 20, 20, 0.45);
  }
  .cover__panel { position: absolute; left: 0; top: 0; }

  .tagline {
    position: absolute; left: 25px; top: 152px;
    color: var(--green); font-size: 29px; font-weight: 400; line-height: 38px;
    letter-spacing: -0.3px; text-transform: uppercase;
  }

  .service { position: absolute; top: 232px; width: 240px; text-align: center; }
  .service__icon { display: block; margin: 0 auto; }
  .service__label {
    display: block; margin-top: 21px;
    color: var(--white); font-size: 23px; font-weight: 400; letter-spacing: 0.2px;
  }
  .service--discovery { left: 423px; }
  .service--strategy { left: 665px; }
  .service--implementation { left: 898px; }

  .brand-box {
    position: absolute; left: 25px; top: 277px; width: 243px; height: 241px;
    background: var(--white); border: 1px solid #c9c9c9; padding: 5px;
  }
  .brand-box__inner {
    width: 100%; height: 100%; background: var(--ink);
    display: flex; align-items: center; justify-content: center; gap: 14px;
  }
  .brand-box__dot { width: 34px; height: 34px; background: var(--green); }
  .brand-box__name { color: var(--white); font-size: 46px; font-weight: 700; letter-spacing: 1px; }

  .actions { position: absolute; top: 472px; left: 821px; display: flex; gap: 18px; }
  .btn {
    height: 35px; display: flex; align-items: center; padding: 0 12px;
    background: var(--btn-bg); border: 1px solid var(--btn-border); border-radius: 2px;
    color: var(--btn-text); font-size: 17px; font-weight: 700;
  }
  .btn-group { display: flex; }
  .btn-group .btn + .btn { border-left: none; padding: 0 10px; gap: 6px; }
</style>
</head>
<body>
  <section class="cover">
    <div class="cover__photo" role="img" aria-label="Black and white team photo of five smiling young financial planners standing together"></div>
    <div class="cover__band"></div>

    <svg class="cover__panel" width="420" height="450" viewBox="0 0 420 450" aria-hidden="true">
      <path d="M0 0 H388 V260 C388 360 330 440 262 450 H0 Z" fill="var(--green)"/>
      <path d="M0 0 H372 V255 C372 350 318 430 250 450 H0 Z" fill="var(--ink)"/>
    </svg>

    <p class="tagline">Secure future,<br>enhanced lifestyle</p>

    <div class="service service--discovery">
      <svg class="service__icon" width="146" height="146" viewBox="0 0 146 146" aria-hidden="true">
        <defs>
          <linearGradient id="g1" x1="0" y1="0" x2="0" y2="1">
            <stop offset="0" stop-color="var(--green-light)"/>
            <stop offset="1" stop-color="var(--green-deep)"/>
          </linearGradient>
        </defs>
        <circle cx="73" cy="73" r="70" fill="url(#g1)" stroke="#9fe07f" stroke-width="2"/>
        <g fill="none" stroke="var(--white)" stroke-width="6" stroke-linecap="round">
          <path d="M58 36 H88 M58 47 H88 M58 58 H88 M60 69 H86"/>
        </g>
        <path d="M56 76 H90 L86 90 L82 96 H64 L60 90 Z" fill="var(--white)"/>
        <path d="M62 100 H84 V112 Q73 120 62 112 Z" fill="var(--white)"/>
      </svg>
      <span class="service__label">DISCOVERY</span>
    </div>

    <div class="service service--strategy">
      <svg class="service__icon" width="146" height="146" viewBox="0 0 146 146" aria-hidden="true">
        <defs>
          <linearGradient id="g2" x1="0" y1="0" x2="0" y2="1">
            <stop offset="0" stop-color="var(--green-light)"/>
            <stop offset="1" stop-color="var(--green-deep)"/>
          </linearGradient>
        </defs>
        <circle cx="73" cy="73" r="70" fill="url(#g2)" stroke="#9fe07f" stroke-width="2"/>
        <g fill="none" stroke="var(--white)" stroke-linecap="round">
          <circle cx="70" cy="72" r="30" stroke-width="5"/>
          <circle cx="70" cy="72" r="18" stroke-width="5"/>
          <path d="M70 72 L104 40" stroke-width="4"/>
          <path d="M98 38 L106 30 M106 42 L114 36" stroke-width="4"/>
          <path d="M52 108 L46 118 M70 108 V120 M88 108 L94 118" stroke-width="4"/>
        </g>
        <circle cx="70" cy="72" r="6" fill="var(--white)"/>
      </svg>
      <span class="service__label">STRATEGY</span>
    </div>

    <div class="service service--implementation">
      <svg class="service__icon" width="146" height="146" viewBox="0 0 146 146" aria-hidden="true">
        <defs>
          <linearGradient id="g3" x1="0" y1="0" x2="0" y2="1">
            <stop offset="0" stop-color="var(--green-light)"/>
            <stop offset="1" stop-color="var(--green-deep)"/>
          </linearGradient>
        </defs>
        <circle cx="73" cy="73" r="70" fill="url(#g3)" stroke="#9fe07f" stroke-width="2"/>
        <g stroke="var(--white)" stroke-linecap="round" fill="none">
          <path d="M48 44 L100 104" stroke-width="12"/>
          <path d="M100 44 L52 100" stroke-width="9"/>
        </g>
        <path d="M38 36 L50 32 L58 44 L48 52 L36 46 Z" fill="var(--white)"/>
        <circle cx="104" cy="40" r="14" fill="var(--white)"/>
        <circle cx="110" cy="34" r="7" fill="var(--green-deep)"/>
      </svg>
      <span class="service__label">IMPLEMENTATION</span>
    </div>
  </section>

  <div class="brand-box">
    <div class="brand-box__inner">
      <span class="brand-box__dot"></span>
      <span class="brand-box__name">KMRT</span>
    </div>
  </div>

  <div class="actions">
    <span class="btn">Update Info</span>
    <div class="btn-group">
      <span class="btn">Activity Log</span>
      <span class="btn">
        <svg width="14" height="14" viewBox="0 0 14 14" aria-hidden="true">
          <circle cx="7" cy="7" r="4.5" fill="none" stroke="#333" stroke-width="2.4" stroke-dasharray="2.2 1.3"/>
          <circle cx="7" cy="7" r="1.6" fill="#333"/>
        </svg>
        <svg width="12" height="8" viewBox="0 0 12 8" aria-hidden="true"><path d="M0 0 H12 L6 7 Z" fill="#5b74a8"/></svg>
      </span>
    </div>
  </div>
</body>
</html>
```